New Innovative Counselling and psychotherapy Service needs Business Card design

Keep it simple and professional. On one side, just company name and logo (perhaps in all blue) and maybe a tag line.

On other side (all white) my name and Qualifications in centre

Industry/Entity Type

Health And Wellness

Contact Information for Business Card

Derek Hollis
Counsellor & Psychotherapist
BSc (Psychol.), BA, Dip. (Couns. & Psych.), PG.Cert (CBT), ADLnR, ESGW

I will also require Mobile no, Email and web site address of which I'll pass on to final designer.

Font styles to use
Sans Serif

Requirements
Must have
• My Logo Only and please use the colours in logo that is in it.
Should not have
• Any other images

```html
<!DOCTYPE html>
<html lang="en">
<head>
<meta charset="utf-8">
<title>Kindred Lane – Business Card</title>
<link rel="stylesheet" href="https://fonts.googleapis.com/css2?family=Arimo:wght@400;700&display=swap">
<style>
  :root {
    --page-bg: #e9e6e1;
    --card-white: #ffffff;
    --card-dark: #333333;
    --brand-blue: #3fa9f0;
    --brand-green: #8cc63f;
    --text-grey: #555555;
    --text-light: #f4f4f4;
  }
  * { margin: 0; padding: 0; box-sizing: border-box; }
  html, body {
    width: 1200px;
    height: 950px;
    overflow: hidden;
    background: var(--page-bg);
    font-family: "Arimo", Arial, sans-serif;
  }
  .canvas {
    position: relative;
    width: 1200px;
    height: 950px;
  }
  .card {
    position: absolute;
    top: 325px;
    width: 520px;
    height: 300px;
    border-radius: 26px;
    box-shadow: 0 6px 18px rgba(0, 0, 0, 0.18);
  }
  .card--front {
    left: 60px;
    background: var(--card-white);
    display: flex;
    flex-direction: column;
    align-items: center;
    justify-content: center;
    text-align: center;
    padding: 0 24px;
  }
  .card--back {
    left: 620px;
    background: var(--card-dark);
    display: flex;
    flex-direction: column;
    align-items: center;
    justify-content: center;
  }
  .holder-name {
    color: var(--brand-blue);
    font-weight: 700;
    font-size: 30px;
    margin-bottom: 8px;
  }
  .holder-role {
    color: var(--brand-green);
    font-weight: 700;
    font-size: 18px;
    margin-bottom: 6px;
  }
  .holder-qualifications {
    color: var(--brand-green);
    font-weight: 700;
    font-size: 12.5px;
    margin-bottom: 12px;
  }
  .holder-contact {
    color: var(--text-grey);
    font-size: 14px;
    line-height: 1.45;
  }
  .brand {
    display: flex;
    align-items: center;
    gap: 16px;
    margin-bottom: 22px;
  }
  .brand-dot {
    width: 44px;
    height: 44px;
    border-radius: 50%;
    background: var(--brand-blue);
  }
  .brand-name {
    color: var(--text-light);
    font-size: 44px;
    font-weight: 400;
  }
  .tagline {
    color: var(--text-light);
    font-size: 14px;
  }
</style>
</head>
<body>
<main class="canvas">
  <section class="card card--front">
    <h1 class="holder-name">Derek Hollis</h1>
    <p class="holder-role">Counsellor &amp; Psychotherapist</p>
    <p class="holder-qualifications">BSc (Psychol.), BA, Dip. (Couns. &amp; Psych.) PG.Cert (CBT), ADLnR, ESGW</p>
    <p class="holder-contact">M. 555 210 4873&nbsp; E. derek@kindredlane.com<br>W. www.kindredlane.com</p>
  </section>
  <section class="card card--back">
    <div class="brand">
      <span class="brand-dot"></span>
      <span class="brand-name">Kindred Lane</span>
    </div>
    <p class="tagline">Steady Support For A Calmer And Healthier Mind</p>
  </section>
</main>
</body>
</html>
```